Manuka honey wholesales and export company needs a website

We are a Manuka honey Wholesale and export company based in New Zealand and needing a website to attract new clients.
We produce one of the worlds best honeys so we need a clean, modern look that lets everybody know that we can supply our product around the world.
We source only the finest Manuka honey from some of the most remote parts of New Zealand and send it around the world for everyone to enjoy.
We need a website that will allow people to inquire about export or bulk purchasing as well as a buying tab with pricing but one that we can add photos to as our product labels are not complete yet.
We also support and supply local farmers markets and a page dedicated to this would be good with details on when and where they are.

Here are links to other manuka honey websites to get an idea
http://www.petalgrove.example.nz/
http://www.dalvoren.example.nz/key-ingredients/manuka-honey/nz200417?gclid=Tq8WLPmZrsXDNQBYehFK27JtRBOzZvWqKx3HTRnYV5Pd83UkMqWfjLeS64-jqVXNcEAbsGLy0nTpbYcQoFxZ4M7YLRC

Target Market(s)

The general public, retail shops and exporters

Industry/Entity Type

Health And Wellness

Number of Pages Required

5+ page

Font styles to use
Serif

Requirements
Must have
• 1. A page and contact details for Export and wholesale inquiries
• Tobias Frennick
• Export manager
• +64 21 830 419
• tbfrennick@mailvista.example.nz
• 2. Page for the farmers market we supply our product to.
• Details....
• Contact: Owen Pascoe
• +64 21 648 1073
• kettlebloomnz@postbay.example.com
• MARKET INFORMATION
• Harbourlight Market
• The market operates year round and is located on Fenwick Square.*
• http://harbourlight.example.org/le-pavot-market/
• Saturday 8am-1pm
• Sunday 9am-1pm
• Ashgrove Village Market
• http://www.ashgrovefarmersmarket.example.nz/
• 42 Larchmont Rd, Ashgrove, Auckland 2591, New Zealand
• Market is held each Sunday from 8:30am-1pm.
• 3. An information page on manuka honey....i will attach info but most of the info you can find on other manuka honey websites..
• Health benefits..
• There are two main components of Manuka honey which give it many health benefits:
• - Hydrogen peroxide, a naturally antibiotic found in Manuka honey.
• - Methylglyoxal (MG). A powerful antibiotic compound found in large quantities in Manuka honey.
• What is MGO?
• The MGO indicates the amount of Methylglyoxal in the honey. The higher the MGO rating the more antibacterial properties are in the honey.
• Proven health Benefits of Active Manuka are....
• Aiding in the treatment of:
• - -Common Cold and Flu
• - -sore throats
• - -cuts and abrasions
• - -Reduce hair loss and scalp problems
• - -treating fungal infections
• - -Burns
• - -ulsers
• - -strengthening the immune system
• 4. A product page with a range of our products with a link yo by direct from us
• The details for this page will need to be added later as we are still doing our range!
Nice to have
• Feel free to make up a mission statement or whatever inspires you to make this a great website.
Should not have
• Go crazy please! I trust you will come up with something amazing :)

```html
<!DOCTYPE html>
<html lang="en">
<head>
<meta charset="utf-8">
<title>Kettlebloom Honey NZ Limited</title>
<link href="https://fonts.googleapis.com/css2?family=Poiret+One&family=Open+Sans:wght@300;400;600&display=swap" rel="stylesheet">
<style>
:root{
  --yellow:#ecd100;
  --dark:#333333;
  --ink:#3a3a3a;
  --muted:#6d6d6d;
  --grey-panel:#f2f2f2;
  --white:#ffffff;
  --hero-a:#5b4a2c;
  --hero-b:#b88a3c;
  --hero-c:#3a2d1a;
}
*{box-sizing:border-box;margin:0;padding:0}
html,body{width:707px;height:1200px;overflow:hidden;background:var(--white)}
body{position:relative;font-family:"Open Sans",Arial,sans-serif;color:var(--ink)}
.abs{position:absolute}
.display{font-family:"Poiret One","Century Gothic",sans-serif}
a{color:inherit;text-decoration:none}

/* hero */
.hero-photo{left:0;top:0;width:707px;height:316px;
  background:radial-gradient(ellipse at 70% 40%,#c99a4a 0%,transparent 55%),
  linear-gradient(120deg,#7d6a3e 0%,var(--hero-a) 35%,var(--hero-b) 70%,var(--hero-c) 100%)}
.site-header{left:0;top:0;width:707px;height:56px;background:rgba(40,32,20,.55)}
.brand{left:92px;top:34px;display:flex;align-items:center;gap:5px;color:var(--white);font-size:12px}
.brand-dot{width:9px;height:9px;border-radius:50%;background:var(--yellow)}
.nav{left:254px;top:24px;display:flex;gap:0;font-size:7.6px;color:var(--white)}
.nav a{position:absolute;white-space:nowrap}
.nav .active{color:var(--yellow)}
.nav .active::before{content:"";position:absolute;left:-7px;top:-24px;width:46px;height:2px;background:var(--yellow)}
.quote-btn{left:486px;top:19px;width:84px;height:21px;border:1px solid var(--yellow);border-radius:11px;color:var(--white);font-size:7.6px;display:flex;align-items:center;justify-content:center}
.cart{left:586px;top:18px}
.hero-title{left:0;width:707px;top:146px;text-align:center;color:var(--white);font-size:24px}
.hero-sub{left:0;width:707px;top:177px;text-align:center;color:var(--white);font-size:11px}
.outline-btn{border:1.5px solid var(--yellow);border-radius:12px;display:flex;align-items:center;justify-content:center;font-size:8px}
.hero-btn{left:289px;top:209px;width:85px;height:20px;color:var(--white)}

/* manuka intro */
.jars-illustration{left:380px;top:316px;width:327px;height:263px;
  background:radial-gradient(ellipse at 55% 60%,#f0a420 0%,#f6c75e 35%,rgba(255,255,255,0) 70%)}
.section-title{font-size:17px;color:var(--ink)}
.lead{font-size:11.6px;line-height:15px;color:#555;font-weight:300}
.body-copy{font-size:7px;line-height:10.3px;color:#666}
.solid-btn{background:var(--yellow);border-radius:11px;display:flex;align-items:center;justify-content:center;font-size:8px;color:var(--ink)}
.pdf-link{font-size:7.4px;color:var(--ink);display:flex;align-items:center;gap:4px}

/* product band */
.product-photo{left:0;top:579px;width:707px;height:259px;
  background:radial-gradient(ellipse at 30% 50%,#2a1a12 0%,#3a2a22 22%,rgba(0,0,0,0) 42%),
  linear-gradient(90deg,#6d6a66 0%,#8a8680 40%,#6f7065 75%,#55594b 100%)}

/* quote form */
.quote-card{left:406px;top:551px;width:209px;height:316px;background:var(--yellow);border-radius:4px;overflow:hidden;box-shadow:0 3px 8px rgba(0,0,0,.2)}
.quote-card svg{position:absolute;left:0;top:0}
.quote-title{left:0;width:209px;top:12px;text-align:center;color:var(--white);font-size:17px}
.quote-sub{left:30px;width:149px;top:35px;text-align:center;color:var(--white);font-size:6.2px;line-height:8px}
.field{left:19px;width:171px;height:19px;background:var(--white);border:1px solid #e0c800;font-size:6.6px;color:#777;padding:5px 8px}
.send-btn{left:69px;top:267px;width:71px;height:20px;border:1.3px solid var(--ink);border-radius:11px;font-size:8px;display:flex;align-items:center;justify-content:center;gap:5px}

/* about + contact */
.contact-panel{left:378px;top:838px;width:329px;height:291px;background:var(--grey-panel)}
.accent{color:var(--yellow)}
.contact-rule{left:406px;top:927px;width:209px;height:1px;background:#c9c9c9}
.contact-group{font-size:7px;color:var(--ink);line-height:10.5px}
.contact-group .role{color:var(--muted)}
.contact-group .phone{font-size:8.6px;color:#555}
.contact-group .mail{color:#555;text-decoration:underline}
.social{top:1070px;width:22px;height:22px;border:1px solid var(--yellow);border-radius:50%}
.social.active{background:var(--yellow)}
.social::after{content:"";position:absolute;left:9px;top:9px;width:4px;height:4px;border-radius:50%;background:var(--ink)}

/* footer */
.site-footer{left:0;top:1129px;width:707px;height:71px;background:var(--dark)}
.footer-mark{left:96px;top:1157px;width:14px;height:14px;border-radius:50%;background:var(--yellow)}
.copyright{left:138px;top:1154px;font-size:7.2px;color:var(--white)}
.legal{left:138px;top:1166px;font-size:7px;color:#9a9a9a}
.footer-divider{left:378px;top:1145px;width:1px;height:38px;background:#555}
.payments{left:406px;top:1158px;display:flex;gap:3px}
.card{width:23px;height:15px;background:var(--white);border-radius:2px;font-size:5px;color:var(--dark);display:flex;align-items:center;justify-content:center;font-weight:600}
.to-top{left:608px;top:1157px}
</style>
</head>
<body>

<!-- Hero -->
<div class="abs hero-photo" role="img" aria-label="Close-up photo of honey bees flying around a hive"></div>
<header class="abs site-header"></header>
<div class="abs brand"><span class="brand-dot"></span><span>Kettlebloom Honey NZ Limited</span></div>
<nav class="abs nav">
  <a class="active" style="left:0">About Us</a>
  <a style="left:46px">Manuka Honey</a>
  <a style="left:112px">Online Store</a>
  <a style="left:171px">Contact Us</a>
</nav>
<a class="abs quote-btn">Get Free Quote</a>
<svg class="abs cart" width="30" height="26" viewBox="0 0 30 26" aria-label="Cart">
  <path d="M1 5h4l3 12h13l3-9H7" fill="none" stroke="#fff" stroke-width="1.3"/>
  <circle cx="10" cy="21" r="1.6" fill="#fff"/><circle cx="19" cy="21" r="1.6" fill="#fff"/>
  <circle cx="24" cy="4" r="4" fill="#ecd100"/>
  <text x="24" y="5.6" font-size="4.5" text-anchor="middle" fill="#333" font-family="Open Sans,sans-serif">02</text>
</svg>
<h1 class="abs hero-title display">Kettlebloom Honey NZ Limites</h1>
<p class="abs hero-sub">We produce one of the worlds best Manuka Honey for you</p>
<a class="abs outline-btn hero-btn">Discover More</a>

<!-- Manuka intro -->
<div class="abs jars-illustration" role="img" aria-label="Illustration of honey jars with a wooden dipper, daisies and clover"></div>
<h2 class="abs section-title display" style="left:92px;top:358px">Manuka Honey</h2>
<p class="abs lead" style="left:92px;top:383px;width:270px">Deliciously good Manuka honey from NZ's most remote, pristine locations.</p>
<p class="abs body-copy" style="left:92px;top:428px;width:270px">It is a long established fact that a reader will be distracted by the readable content of a page when looking at its layout. The point of using lorem ipsum is that it has a more-or-less normal distribution of letters, as opposed to using Content here,content here', making it look like ...</p>
<a class="abs solid-btn" style="left:92px;top:492px;width:85px;height:22px">Explore More</a>
<a class="abs pdf-link" style="left:196px;top:498px">
  <svg width="8" height="8" viewBox="0 0 8 8"><path d="M4 0v5M1.5 3l2.5 2.5L6.5 3M0.5 7.5h7" stroke="#333" stroke-width="1.2" fill="none"/></svg>
  <span style="text-decoration:underline">Health Benefits Pdf</span>
</a>

<!-- Product band -->
<div class="abs product-photo" role="img" aria-label="Photo of dark Manuka honey jars on weathered wood with bees"></div>

<!-- Quote form -->
<form class="abs quote-card">
  <svg width="209" height="72" viewBox="0 0 209 72"><path d="M0 0h209v52Q104.5 80 0 52Z" fill="#333"/></svg>
  <h3 class="abs quote-title display">Request A Quote</h3>
  <p class="abs quote-sub">Lorem Ipsum has been the industry's standard dummy text ever</p>
  <div class="abs field" style="top:86px">Name</div>
  <div class="abs field" style="top:112px">Email</div>
  <div class="abs field" style="top:139px">Phone</div>
  <div class="abs field" style="top:166px">Who are you?
    <svg style="position:absolute;right:7px;top:7px" width="6" height="4" viewBox="0 0 6 4"><path d="M0.5 0.5L3 3l2.5-2.5" stroke="#777" fill="none"/></svg>
  </div>
  <div class="abs field" style="top:193px;height:58px">Message</div>
  <div class="abs send-btn"><span style="width:6px;height:6px;border-radius:50%;background:#333"></span>Send</div>
</form>

<!-- About -->
<div class="abs contact-panel"></div>
<h2 class="abs section-title display" style="left:92px;top:900px">Kettlebloom <span class="accent">Honey NZ Limites</span></h2>
<p class="abs lead" style="left:92px;top:926px;width:270px">We are a Manuka honey Wholesale and export company based in New Zealand.</p>
<p class="abs body-copy" style="left:92px;top:965px;width:272px">We produce one of the worlds best honeys so we need a clean, modern look that lets everybody know that we can supply our product around the world. We source only the finest Manuka honey from some of the most remote parts of New Zealand and send it around the world for everyone to enjoy.</p>
<p class="abs body-copy" style="left:92px;top:1017px;width:272px">Lorem Ipsum has been the industry's standard dummy text ever since the 1500s, when an unknown printer took a galley of type and scrambled it to make a type specimen book.</p>
<a class="abs outline-btn" style="left:92px;top:1070px;width:85px;height:21px;color:var(--ink)">Discover More</a>

<!-- Contact -->
<h2 class="abs section-title display" style="left:406px;top:900px">Contact Us</h2>
<div class="abs contact-rule"></div>
<div class="abs contact-group" style="left:406px;top:939px">
  <div>Export and Wholesale</div>
  <div class="role" style="margin-top:3px">Tobias Frennick&nbsp; / &nbsp;Export manager</div>
  <div class="phone">+64 21 830 419</div>
  <div class="mail">tbfrennick@mailvista.example.nz</div>
</div>
<div class="abs contact-group" style="left:406px;top:1002px">
  <div>Farmers Market</div>
  <div class="role" style="margin-top:3px">Owen Pascoe&nbsp; / &nbsp;Product Supplyer</div>
  <div class="phone">+64 21 648 1073</div>
  <div class="mail">kettlebloomnz@postbay.example.com</div>
</div>
<a class="abs social active" style="left:405px" aria-label="Social link 1"></a>
<a class="abs social" style="left:431px" aria-label="Social link 2"></a>
<a class="abs social" style="left:457px" aria-label="Social link 3"></a>
<a class="abs social" style="left:483px" aria-label="Social link 4"></a>

<!-- Footer -->
<footer class="abs site-footer"></footer>
<div class="abs footer-mark"></div>
<p class="abs copyright">© Kettlebloom <span class="accent">Honey NZ Limites.</span> All Rights Reserved</p>
<p class="abs legal">Shipping &amp; Delivery &nbsp;|&nbsp; Terms &amp; Conditions &nbsp;|&nbsp; Privacy Policy</p>
<div class="abs footer-divider"></div>
<div class="abs payments">
  <span class="card">Paylo</span><span class="card">Cardix</span><span class="card">Mintro</span><span class="card">Voyant</span>
</div>
<svg class="abs to-top" width="10" height="16" viewBox="0 0 10 16" aria-label="Back to top"><path d="M5 15V2M1 6l4-4 4 4" stroke="#ecd100" stroke-width="1.6" fill="none"/></svg>

</body>
</html>
```